Business Card design for amazing new Dental Office

Please read this brief closely!

Our client is a modern new dental office/
They love their new logo.
Now it's time to create a business card for them.

It should be a two sided card:
Side one should have the logo and name and maybe a color background or design.
Side two should have all the contact information which is here:

Marcus Pellow, D.D.S
General and Cosmetic Dentistry
4178 W. Orchard Lane
Ventura, CA 93017
(805) 219-4862
drmarc@bluefernsmiles.example
www.bluefernsmiles.example

Feel free to arrange that info as you like and to style both sides of the card according to your creativity. This is a chance for you to show your design skills!

Client is open to font choices and is looking for a style that is amazing and premium. Colors can be selected from the logo, or any variation of those.

You will not win this contest with a less than beautiful card design so please feel free to make multiple submissions.

Logo files attached and please message me with any questions.
Thanks!

Target Market(s)

Families and Professionals seeking dental services

Industry/Entity Type

Dental

Contact Information for Business Card

Logo, style, contact info as per the brief

Font styles to use
Sans Serif

Requirements
Must have
• Client's logo and contact details as per brief
Nice to have
• Unique style reflecting high end dental clinic near the beach
Should not have
• Must not look like a template

```html
<!DOCTYPE html>
<html lang="en">
<head>
<meta charset="utf-8">
<title>Blue Fern Smiles – Business Card</title>
<link rel="stylesheet" href="https://fonts.googleapis.com/css2?family=Josefin+Sans:wght@300;400&family=Open+Sans:wght@400&display=swap">
<style>
  :root {
    --stage: #2b2b2b;
    --card-front: #050505;
    --card-back-start: #1c1e1e;
    --card-back-end: #080808;
    --swoosh: #1a1a1a;
    --swoosh-light: #222222;
    --brand-text: #d6d8d8;
    --gold: #cdb42a;
    --body-text: #d4d4d4;
    --icon: #4fb3d6;
    --mark: #4aa9cf;
  }
  * { margin: 0; padding: 0; box-sizing: border-box; }
  html, body { width: 1200px; height: 732px; overflow: hidden; }
  body { background: var(--stage); position: relative; font-family: "Open Sans", sans-serif; }

  .card {
    position: absolute;
    top: 242px;
    width: 436px;
    height: 248px;
    box-shadow: 0 6px 14px rgba(0,0,0,0.55);
    overflow: hidden;
  }
  .card--contact { left: 144px; background: var(--card-front); }
  .card--brand {
    left: 621px;
    background: linear-gradient(100deg, var(--card-back-start) 0%, #121414 55%, var(--card-back-end) 100%);
  }

  .brand {
    position: absolute;
    display: flex;
    align-items: center;
    gap: 8px;
    font-family: "Josefin Sans", sans-serif;
    font-weight: 300;
    color: var(--brand-text);
    white-space: nowrap;
    letter-spacing: 1.5px;
  }
  .brand__dot {
    width: 10px; height: 10px; border-radius: 50%;
    background: var(--mark);
    flex: none;
  }
  .card--contact .brand { left: 18px; top: 84px; font-size: 21px; }
  .card--brand .brand { left: 50%; top: 140px; transform: translateX(-50%); font-size: 24px; }

  .person { position: absolute; left: 230px; top: 84px; }
  .person__name {
    font-family: "Josefin Sans", sans-serif;
    font-weight: 400;
    font-size: 14px;
    color: var(--gold);
    letter-spacing: 0.4px;
  }
  .person__role { font-size: 9.6px; color: var(--body-text); margin-top: 1px; letter-spacing: 0.2px; }

  .contact-list { position: absolute; left: 230px; top: 125px; list-style: none; }
  .contact-list li {
    display: flex; align-items: center; gap: 6px;
    font-size: 9.8px; color: var(--body-text); height: 13.2px;
  }
  .contact-list svg { width: 9px; height: 9px; flex: none; }

  .swoosh { position: absolute; left: 0; bottom: 0; width: 436px; height: 50px; }

  .address {
    position: absolute; left: 230px; top: 222px;
    font-size: 9.6px; color: #ececec; letter-spacing: 0.1px;
  }
</style>
</head>
<body>

  <section class="card card--contact">
    <div class="brand"><span class="brand__dot"></span>Blue Fern Smiles</div>

    <div class="person">
      <p class="person__name">Marcus Pellow, D.D.S</p>
      <p class="person__role">General and Cosmetic Dentistry</p>
    </div>

    <ul class="contact-list">
      <li>
        <svg viewBox="0 0 10 10" fill="none" stroke="var(--icon)" stroke-width="0.9"><path d="M2 1.2 L3.6 1 L4.4 3 L3.4 3.8 Q4.3 5.7 6.2 6.6 L7 5.6 L9 6.4 L8.8 8 Q5 8.6 1.4 4.8 Q1 3 2 1.2 Z"/></svg>
        (805) 219-4862
      </li>
      <li>
        <svg viewBox="0 0 10 10" fill="none" stroke="var(--icon)" stroke-width="0.9"><rect x="0.8" y="2" width="8.4" height="6" /><path d="M0.8 2 L5 5.4 L9.2 2"/></svg>
        drmarc@bluefernsmiles.example
      </li>
      <li>
        <svg viewBox="0 0 10 10" fill="none" stroke="var(--icon)" stroke-width="0.9"><circle cx="5" cy="5" r="4.2"/><ellipse cx="5" cy="5" rx="1.8" ry="4.2"/><path d="M0.8 5 H9.2 M1.6 3 H8.4 M1.6 7 H8.4"/></svg>
        www.bluefernsmiles.example
      </li>
    </ul>

    <svg class="swoosh" viewBox="0 0 436 50" preserveAspectRatio="none" aria-hidden="true">
      <path d="M0 25 Q120 22 230 8 Q330 -2 436 10 L436 50 L0 50 Z" fill="var(--swoosh-light)"/>
      <path d="M0 36 Q140 32 250 16 Q350 6 436 14 L436 50 L0 50 Z" fill="var(--swoosh)"/>
    </svg>

    <p class="address">4178 W. Orchard Lane, Ventura, CA 93017</p>
  </section>

  <section class="card card--brand">
    <div class="brand"><span class="brand__dot"></span>Blue Fern Smiles</div>
  </section>

</body>
</html>
```